Publishing company needs book cover for multi-author book

Copperleaf Lantern Publishing needs a book cover designed for a multi-author book called Quiet Orbits: Uncommon Triumph Tales from Remarkable Pathfinders. We would like to see designs that incorporates the design theme of the image attached and possibly the image itself. The book will be used by the contributing authors who are  are Healers, Psychics, Coaches, Energy Workers, Astrologers, Numerologist, Tarot Card Readers and will be using this book to both market their business and use in their practices.  The final design should communicate  these spiritual practices.
I would love to see
1. A silhouette or image of a woman holding a ball or circle with the attached art inside of.
2. The concepts in the attached art brought into a  new design or  enhancing the original art.

Target Market(s)
The clients and audiences of the contributing authors
Industry/Entity Type
Spiritual, Body Mind Spirit, Evolving Continuousness, Alternative Healing
Colors
Designer to choose colors to be used in the design.
Requirements
Must have
- Title- Quiet Orbits: Uncommon Triumph Tales from Remarkable Pathfinders. and the name of the publishing company: Copperleaf Lantern Publishing

Nice to have
- I would love to have the concept of the artwork coming to life through an image of woman, visionary, healer who is healing the world through her modalities.

Should not have
- Dimensions - 6X9

```html
<!DOCTYPE html>
<html lang="en">
<head>
<meta charset="utf-8">
<title>Quiet Orbits – Book Cover</title>
<link rel="stylesheet" href="https://fonts.googleapis.com/css2?family=Barlow+Condensed:wght@600&family=Black+Ops+One&display=swap">
<style>
  :root {
    --page-bg: #ffffff;
    --cover-navy: #0a1530;
    --cover-deep: #060e22;
    --mosaic-pale: #a9d3d6;
    --mosaic-teal: #5fa3a8;
    --mosaic-sea: #3c7f86;
    --mosaic-blue: #1f4fa0;
    --mosaic-royal: #173f8c;
    --mosaic-green: #7fa56c;
    --mosaic-olive: #5d6e3a;
    --paint-blue: #153f96;
    --paint-lime: #c3dc2c;
    --paint-ice: #9fdbe4;
    --title-blue: #7fb8c4;
    --title-green: #86b817;
    --text-light: #ececec;
    --text-shadow: rgba(0, 0, 0, 0.9);
  }
  html, body {
    margin: 0;
    width: 1200px;
    height: 1200px;
    overflow: hidden;
    background: var(--page-bg);
  }
  .cover {
    position: absolute;
    left: 259px;
    top: 75px;
    width: 689px;
    height: 981px;
    background: var(--cover-navy);
    overflow: hidden;
  }
  .cover__mosaic-art {
    position: absolute;
    left: 0;
    top: 0;
    width: 689px;
    height: 640px;
    background:
      radial-gradient(ellipse 14% 12% at 32% 36%, var(--mosaic-pale), transparent 100%),
      radial-gradient(ellipse 12% 10% at 58% 28%, rgba(169,211,214,0.85), transparent 100%),
      radial-gradient(ellipse 10% 10% at 76% 48%, rgba(169,211,214,0.75), transparent 100%),
      radial-gradient(ellipse 9% 8% at 20% 58%, rgba(169,211,214,0.7), transparent 100%),
      radial-gradient(ellipse 10% 9% at 44% 78%, rgba(169,211,214,0.6), transparent 100%),
      radial-gradient(ellipse 12% 10% at 88% 72%, rgba(127,165,108,0.8), transparent 100%),
      radial-gradient(ellipse 14% 12% at 14% 80%, rgba(93,110,58,0.8), transparent 100%),
      radial-gradient(ellipse 16% 12% at 70% 16%, rgba(127,165,108,0.65), transparent 100%),
      radial-gradient(ellipse 46% 40% at 52% 48%, var(--mosaic-teal) 0%, var(--mosaic-sea) 45%, rgba(31,79,160,0.6) 80%, transparent 100%),
      linear-gradient(160deg, var(--mosaic-blue) 0%, var(--mosaic-royal) 45%, #143072 75%, var(--cover-navy) 100%);
  }
  .cover__paint-art {
    position: absolute;
    left: 0;
    bottom: 0;
    width: 689px;
    height: 460px;
    background:
      radial-gradient(ellipse 18% 10% at 16% 84%, var(--paint-lime), transparent 100%),
      radial-gradient(ellipse 10% 6% at 98% 22%, rgba(195,220,44,0.6), transparent 100%),
      radial-gradient(ellipse 12% 12% at 76% 74%, var(--paint-ice), transparent 100%),
      radial-gradient(ellipse 10% 8% at 92% 90%, rgba(159,219,228,0.6), transparent 100%),
      radial-gradient(ellipse 40% 22% at 50% 96%, var(--paint-blue), transparent 100%),
      linear-gradient(180deg, rgba(6,14,34,0) 0%, var(--cover-deep) 22%, #0c2360 62%, #143a8c 100%);
  }
  .cover__publisher {
    position: absolute;
    top: 16px;
    left: 0;
    right: 0;
    margin: 0;
    text-align: center;
    font-family: "Barlow Condensed", sans-serif;
    font-weight: 600;
    font-size: 17px;
    letter-spacing: 3px;
    color: var(--text-light);
    text-shadow: 0 0 6px var(--text-shadow);
  }
  .cover__subtitle {
    position: absolute;
    top: 558px;
    left: 0;
    right: 0;
    margin: 0;
    text-align: center;
    font-family: "Barlow Condensed", sans-serif;
    font-weight: 600;
    font-size: 39px;
    line-height: 44px;
    color: var(--text-light);
    text-shadow: 0 0 10px var(--text-shadow), 0 0 4px var(--text-shadow);
  }
  .cover__title {
    position: absolute;
    top: 668px;
    left: 0;
    right: 0;
    margin: 0;
    text-align: center;
    font-family: "Black Ops One", sans-serif;
    font-weight: 400;
    text-shadow: 4px 6px 8px var(--text-shadow);
  }
  .cover__title-line {
    display: block;
  }
  .cover__title-line--first {
    color: var(--title-blue);
    font-size: 150px;
    line-height: 112px;
  }
  .cover__title-line--second {
    color: var(--title-green);
    font-size: 122px;
    line-height: 100px;
  }
  .cover__author {
    position: absolute;
    top: 929px;
    left: 0;
    right: 0;
    margin: 0;
    text-align: center;
    font-family: "Barlow Condensed", sans-serif;
    font-weight: 600;
    font-size: 42px;
    line-height: 48px;
    letter-spacing: 4px;
    color: var(--text-light);
    text-shadow: 0 0 10px var(--text-shadow);
  }
</style>
</head>
<body>
  <main class="cover">
    <div class="cover__mosaic-art" role="img" aria-label="Stained-glass mosaic artwork of swirling blue, teal and green shapes"></div>
    <div class="cover__paint-art" role="img" aria-label="Abstract painted texture in deep blue with lime and pale ice streaks"></div>
    <p class="cover__publisher">COPPERLEAF LANTERN PUBLISHING</p>
    <p class="cover__subtitle">UNCOMMON TRIUMPH TALES<br>FROM REMARKABLE PATHFINDERS</p>
    <h1 class="cover__title">
      <span class="cover__title-line cover__title-line--first">QUIET</span>
      <span class="cover__title-line cover__title-line--second">ORBITS</span>
    </h1>
    <p class="cover__author">AUTHOR NAME</p>
  </main>
</body>
</html>
```